Webbanner-Design für Online Pfandhaus
Zielgruppe
Online Pfandhaus
Aufgabenstellung
Der Banner für unsere Webseite soll neu gestaltet werden. (Siehe Bilddatei)
Ziel ist es einen schönen, konvertierenden Banner zu gestalten. Der Banner soll sich an die Seite anpassen.
Der Banner wird dann auch für Social Media benötigt.

```html
<!DOCTYPE html>
<html lang="de">
<head>
<meta charset="utf-8">
<title>leihkontor.net – Ihr Online-Pfandhaus</title>
<link rel="stylesheet" href="https://fonts.googleapis.com/css2?family=Oswald:wght@500&family=Signika:wght@400;600&family=Open+Sans:wght@600;700&display=swap">
<style>
:root{
  --brand:#2a3b8f;
  --teal:#2a9d9f;
  --frame:#8e9ccc;
  --text:#1c1c1c;
  --grey:#555a5e;
  --chat:#3fc14e;
  --badge:#d8232a;
}
*{margin:0;padding:0;box-sizing:border-box}
html,body{width:1200px;height:889px;overflow:hidden;background:#fff}
.page{position:relative;width:1200px;height:889px;font-family:"Signika",sans-serif;color:var(--text)}
.topbar{position:absolute;left:0;top:0;width:1200px;height:74px;background:#fff}
.brand{position:absolute;left:70px;top:24px;display:flex;align-items:center;gap:8px;font-weight:600;font-size:19px;color:var(--brand)}
.brand-dot{width:24px;height:24px;border-radius:50%;background:var(--brand)}
.nav{position:absolute;top:24px;left:0;font-family:"Oswald",sans-serif;font-weight:500;font-size:19px;color:var(--brand)}
.nav span{position:absolute;white-space:nowrap}
.hero{position:absolute;left:0;top:74px;width:1200px;height:539px;
  background:linear-gradient(180deg,#c9a58f 0%,#d8b8a6 25%,#c39a80 52%,#b0876a 53%,#a67d5f 75%,#8d6a4f 100%)}
.hero-band{position:absolute;left:0;top:613px;width:1200px;height:20px;background:var(--brand)}
.card{position:absolute;left:84px;top:109px;width:471px;height:456px;border-radius:14px;background:rgba(255,255,255,.72);text-align:center}
.card-title{position:absolute;left:0;width:100%;top:34px;font-weight:600;font-size:58px;line-height:70px;color:var(--brand)}
.card-sub{position:absolute;left:0;width:100%;top:108px;font-size:42px;line-height:52px}
.card-lead{position:absolute;left:0;width:100%;top:160px;font-size:21px;line-height:34px}
.card-question{position:absolute;left:0;width:100%;top:248px;font-size:15px}
.select{position:absolute;left:115px;top:275px;width:138px;height:42px;background:#fff;border-radius:3px;font-size:15px;text-align:left;padding:11px 12px}
.select svg{position:absolute;right:9px;top:17px}
.btn{position:absolute;left:264px;top:275px;width:89px;height:42px;background:var(--teal);color:#fff;border-radius:3px;font-size:15px;line-height:42px}
.card-alt{position:absolute;left:0;width:100%;top:333px;font-size:15.5px}
.card-alt em{font-style:normal;color:var(--chat);font-weight:600}
.member{position:absolute;left:90px;top:388px;width:218px;font-size:12px;line-height:15px;text-align:right}
.member-badge{position:absolute;left:326px;top:372px;width:44px;height:50px;background:var(--badge);border-radius:4px}
.frame{position:absolute;background:#fff;border:9px solid var(--frame)}
.photo{position:absolute;inset:8px}
.chat-btn{position:absolute;left:1108px;top:591px;width:64px;height:64px;border-radius:50%;background:var(--chat);color:#fff;font-size:10px;display:flex;align-items:center;justify-content:center;box-shadow:0 2px 6px rgba(0,0,0,.25)}
.feature{position:absolute;top:672px;width:170px;text-align:center;font-family:"Open Sans",sans-serif;font-weight:600;font-size:17.5px;line-height:25px;color:var(--grey)}
.feature-icon{height:32px;display:flex;align-items:center;justify-content:center;margin-bottom:7px}
.steps-title{position:absolute;left:0;top:795px;width:1200px;text-align:center;font-family:"Open Sans",sans-serif;font-weight:700;font-size:38px;color:#4a4e52}
.step-ring{position:absolute;top:868px;width:68px;height:68px;border-radius:50%;border:6px solid var(--teal)}
</style>
</head>
<body>
<div class="page">
  <header class="topbar">
    <div class="brand"><span class="brand-dot"></span>Leihkontor.net</div>
    <nav class="nav">
      <span style="left:408px">Start</span>
      <span style="left:478px">Anfrage</span>
      <span style="left:567px">Ablauf</span>
      <span style="left:646px">Wissenswertes</span>
      <span style="left:781px">FAQ</span>
      <span style="left:842px">Standorte <svg width="11" height="7" viewBox="0 0 11 7"><path d="M1 1l4.5 4.5L10 1" fill="none" stroke="#2a3b8f" stroke-width="1.6"/></svg></span>
      <span style="left:964px">Kontakt</span>
      <span style="left:1054px">Über uns</span>
    </nav>
  </header>

  <section class="hero" role="img" aria-label="Unscharfer Ladenhintergrund über einem hellen Holzdielenboden"></section>
  <div class="hero-band"></div>

  <div class="card">
    <div class="card-title">leihkontor.net</div>
    <div class="card-sub">Ihr Online-Pfandhaus</div>
    <div class="card-lead">Bei uns erhalten Sie in kürzester Zeit Geld fur<br>Ihre Wertgegenstände.</div>
    <div class="card-question">Weichen Wertgegenstand möchten Sie belehen?</div>
    <div class="select">Schmuck<svg width="13" height="7" viewBox="0 0 13 7"><path d="M1 1l5.5 5L12 1" fill="none" stroke="#666" stroke-width="1.2"/></svg></div>
    <div class="btn">Anfrage</div>
    <div class="card-alt">Alternative können Sie uns auch direkt unter <em>ChatLine</em> kontraktien.</div>
    <div class="member">Wir sind Mitglied im Bundesverband<br>der Leihhäuser e.V.</div>
    <div class="member-badge"></div>
  </div>

  <div class="frame" style="left:853px;top:129px;width:263px;height:288px">
    <div class="photo" role="img" aria-label="Funkelnder geschliffener Diamant" style="background:radial-gradient(ellipse at 60% 35%,#d6dcef,#ffffff 70%)"></div>
  </div>
  <div class="frame" style="left:703px;top:192px;width:207px;height:226px">
    <div class="photo" role="img" aria-label="Gestapelte Goldbarren" style="background:radial-gradient(ellipse at 55% 55%,#c9a23a,#fff 72%)"></div>
  </div>
  <div class="frame" style="left:867px;top:297px;width:207px;height:227px">
    <div class="photo" role="img" aria-label="Haufen goldener Ringe und Schmuckstücke" style="background:radial-gradient(ellipse at 50% 50%,#d4ad55,#fff 70%)"></div>
  </div>
  <div class="frame" style="left:747px;top:332px;width:158px;height:173px">
    <div class="photo" role="img" aria-label="Zwei goldene Armbanduhren" style="background:radial-gradient(ellipse at 50% 55%,#c7b68a,#fff 70%)"></div>
  </div>

  <div class="chat-btn">ChatLine</div>

  <div class="feature" style="left:92px">
    <div class="feature-icon"><svg width="40" height="26" viewBox="0 0 40 26"><rect x="1.5" y="1.5" width="37" height="23" rx="2" fill="none" stroke="#2a3b8f" stroke-width="3"/><circle cx="20" cy="13" r="6" fill="#2a3b8f"/></svg></div>
    schnelle Auszahlung</div>
  <div class="feature" style="left:261px">
    <div class="feature-icon"><svg width="40" height="28" viewBox="0 0 40 28"><path d="M2 6l18-5 18 5-18 6z M4 10l16 5 16-5v15l-16 3-16-3z" fill="#2a3b8f"/></svg></div>
    versichert bis 5000 €</div>
  <div class="feature" style="left:430px">
    <div class="feature-icon"><svg width="32" height="32" viewBox="0 0 32 32"><circle cx="16" cy="16" r="14" fill="none" stroke="#2a3b8f" stroke-width="3"/><path d="M9 16l5 5 9-10" fill="none" stroke="#2a3b8f" stroke-width="3"/></svg></div>
    keine Bonitätsprüfung</div>
  <div class="feature" style="left:599px">
    <div class="feature-icon"><svg width="38" height="30" viewBox="0 0 38 30"><path d="M19 1L1 16h5v13h10v-9h6v9h10V16h5z" fill="#2a3b8f"/></svg></div>
    Abholung von Zuhause</div>
  <div class="feature" style="left:768px">
    <div class="feature-icon"><svg width="40" height="30" viewBox="0 0 40 30"><path d="M2 18l10-10h12l4 4-8 3-4-2-8 10z M38 12L28 22H16l-4-4 8-3 4 2 8-10z" fill="#2a3b8f"/></svg></div>
    100% Diskretion</div>
  <div class="feature" style="left:937px">
    <div class="feature-icon"><svg width="32" height="32" viewBox="0 0 32 32"><circle cx="16" cy="16" r="15" fill="#2a3b8f"/><circle cx="11" cy="12" r="2" fill="#fff"/><circle cx="21" cy="12" r="2" fill="#fff"/><path d="M9 19q7 6 14 0" fill="none" stroke="#fff" stroke-width="2.2"/></svg></div>
    Faire Bewertung</div>

  <div class="steps-title">So funktioniert's:</div>
  <div class="step-ring" style="left:239px"></div>
  <div class="step-ring" style="left:566px"></div>
  <div class="step-ring" style="left:893px"></div>
</div>
</body>
</html>
```